New Lead input page design

Attached is our concept of a new lead input screen for the back-end of our website which is a tool for a loan agent (2 page PDF attached)

1. This is the first of many other data input screen projects for our website, so the designer that ends up with us will have quite a bit of add on new projects.

2. HERE IS THE LINK WITH THE SAMPLE OF ALL THE CURRENT CONTROLS:
http://apps.brimtally.com/controlWidgets.html

3. The colors and hues of: either GREEN & GREYS or BLUE & GREYS.

4. I think some gradients and shadows adds depth and sophistication. Basically trying to get away from old school flat, one dimensional data screen inputs and add some design flare to it.

5. Upon completion we will need the HTML of the design etc and we will code the input fields directly.

6. See attached files for the entire input screen. Please also add the data input space (see sample) to your design.

Thank you

Reason: We are extending the deadline to give us time to ask current designs to complete slight revisions

Reason: Finalizing the selection for one last variation detailed to current designers

```html
<!DOCTYPE html>
<html lang="en">
<head>
<meta charset="utf-8">
<title>Lead Input – Clients</title>
<link href="https://fonts.googleapis.com/css2?family=Lato:wght@400;700;900&display=swap" rel="stylesheet">
<style>
:root{
  --page:#e9edf1;
  --panel:#ffffff;
  --line:#dfe4e9;
  --ink:#1d232a;
  --muted:#6d7a86;
  --section:#5c6b78;
  --value:#737b83;
  --accent:#1a9fe0;
  --teal:#1fc1c7;
  --cell:#f6f8fa;
  --field-top:#cfd6dd;
}
*{box-sizing:border-box;margin:0;padding:0}
html,body{width:1200px;height:1200px;overflow:hidden;background:var(--page)}
body{font-family:"Lato",Arial,sans-serif;color:var(--ink)}
.stage{position:absolute;left:0;top:0;width:1400px;height:1400px;transform:scale(.857143);transform-origin:0 0}
.abs{position:absolute}
.crumbs{left:153px;top:25px;font-size:12px;color:var(--ink)}
.crumbs span{color:#9aa5af}
.help{left:1076px;top:27px;font-size:11px}
.logout{left:1177px;top:21px;width:70px;height:26px;border:1px solid #bfc7cf;border-radius:13px;background:linear-gradient(#fff,#eef1f4);font-size:13px;font-weight:700;display:flex;align-items:center;justify-content:center}
.tab{top:84px;height:44px;background:linear-gradient(#fff,#f3f5f7);border:1px solid var(--line);border-bottom:none;border-radius:3px 3px 0 0;display:flex;align-items:center;font-size:14px;font-weight:700;color:#5c6670;letter-spacing:.2px}
.tab .ic{width:40px;height:100%;border-right:1px solid var(--line);display:flex;align-items:center;justify-content:center;margin-right:14px}
.tab.active{background:#fff;color:var(--ink);height:45px;z-index:2}
.panel{left:121px;top:127px;width:1172px;height:1227px;background:var(--panel);border:1px solid #d6dce2}
.footer{left:122px;top:1260px;width:1170px;height:93px;background:linear-gradient(#f7f9fa,#eceff2);border-top:1px solid var(--line)}
.head-icon{left:187px;top:163px;width:51px;height:48px;border:1px solid var(--line);border-radius:3px;background:linear-gradient(#fff,#f2f4f6);display:flex;align-items:center;justify-content:center}
.title{left:253px;top:174px;font-size:23px;font-weight:900;letter-spacing:.3px}
.rule{height:1px;background:var(--line)}
.section{font-size:16px;font-weight:700;color:var(--section)}
.field{height:40px;display:flex;border:1px solid #d9dfe5;border-top:3px solid var(--field-top);background:#fff;font-size:17px}
.field.focus{border:2px solid #b7d9ef}
.field .ic{width:40px;background:var(--cell);border-right:1px solid var(--line);display:flex;align-items:center;justify-content:center}
.field .lbl{width:var(--lw);padding-left:14px;display:flex;align-items:center;font-weight:700;background:linear-gradient(90deg,#fff,var(--cell));border-right:1px solid var(--line)}
.field .val{flex:1;padding-left:22px;display:flex;align-items:center;color:var(--value)}
.field .val.dark{color:var(--ink)}
.pill{left:711px;top:922px;width:277px;height:46px;border:1px solid var(--line);border-radius:23px;background:linear-gradient(#fff,#f2f4f6);display:flex;align-items:center;font-size:17px;font-weight:700}
.pill .ic{width:60px;height:100%;border-right:1px solid var(--line);display:flex;align-items:center;justify-content:center;margin-right:40px}
.alert{left:185px;top:1128px;width:244px;height:80px;background:#eceff2;border-radius:3px;padding:12px 16px;font-size:14px}
.alert p{margin-top:6px;color:var(--muted);font-size:13px;line-height:18px}
.alert u{text-decoration-color:#aab3bb}
.status{left:190px;top:1277px;font-size:14px;color:var(--section)}
.status .sub{font-size:13px;margin-top:4px}
.status .sub b{font-weight:400;margin-left:16px}
.bar{left:191px;top:1325px;width:194px;height:10px;border-radius:5px;background:#dde2e7}
.bar i{display:block;width:135px;height:100%;border-radius:5px;background:var(--teal)}
.save{left:1062px;top:1287px;width:114px;height:41px;border:1px solid #c3cbd3;border-radius:3px;background:linear-gradient(#fff,#e9edf1);display:flex;align-items:center;justify-content:center;font-size:16px;font-weight:700;color:#5c6670}
svg{display:block}
</style>
</head>
<body>
<div class="stage">
  <div class="abs crumbs">Home <span>» Loan Tool</span></div>
  <div class="abs help">Help &amp; Support</div>
  <div class="abs logout">Logout</div>

  <div class="abs panel"></div>

  <div class="abs tab active" style="left:139px;width:189px"><span class="ic"><svg width="14" height="16" viewBox="0 0 14 16"><circle cx="7" cy="4.5" r="3.5" fill="#1a9fe0"/><path d="M1 15c0-5 12-5 12 0z" fill="#1a9fe0"/></svg></span>LEAD CATEGORY</div>
  <div class="abs tab" style="left:333px;width:167px"><span class="ic"><svg width="14" height="16"><rect x="1" y="1" width="12" height="14" fill="none" stroke="#8a949d"/><path d="M4 5h6M4 8h6M4 11h6" stroke="#8a949d"/></svg></span>STICKY NOTE</div>
  <div class="abs tab" style="left:505px;width:167px"><span class="ic"><svg width="18" height="14"><rect x="1" y="3" width="16" height="10" rx="2" fill="#6d7780"/><rect x="6" y="1" width="6" height="3" fill="#6d7780"/><circle cx="9" cy="8" r="3" fill="#fff"/></svg></span>SNAP SHOT</div>
  <div class="abs tab" style="left:678px;width:124px"><span class="ic"><svg width="16" height="16"><circle cx="8" cy="8" r="7" fill="none" stroke="#6d7780" stroke-width="1.4"/><path d="M8 4v5M8 11v1.5" stroke="#6d7780" stroke-width="1.6"/></svg></span>ALERTS</div>
  <div class="abs tab" style="left:808px;width:156px"><span class="ic"><svg width="14" height="16"><rect x="1" y="1" width="12" height="14" fill="none" stroke="#8a949d"/><path d="M4 5h6M4 8h6M4 11h6" stroke="#8a949d"/></svg></span>LEAD NOTES</div>
  <div class="abs tab" style="left:971px;width:141px"><span class="ic"><svg width="16" height="16"><rect x="1" y="2" width="14" height="13" fill="none" stroke="#6d7780"/><path d="M1 5h14M4 0v4M12 0v4M4 8h2M7 8h2M10 8h2M4 11h2M7 11h2M10 11h2" stroke="#6d7780"/></svg></span>CALENDAR</div>
  <div class="abs tab" style="left:1120px;width:155px"><span class="ic"><svg width="16" height="16"><circle cx="7" cy="7" r="5.5" fill="none" stroke="#6d7780" stroke-width="1.6"/><path d="M11 11l4 4" stroke="#6d7780" stroke-width="2"/></svg></span>SEE RESULTS</div>

  <div class="abs head-icon"><svg width="26" height="22" viewBox="0 0 26 22"><circle cx="17" cy="6" r="4" fill="#1a9fe0"/><path d="M10 20c0-8 14-8 14 0z" fill="#1a9fe0"/><circle cx="9" cy="7" r="4.5" fill="#1680c0"/><path d="M1 21c0-9 16-9 16 0z" fill="#1680c0"/></svg></div>
  <div class="abs title">CLIENTS</div>
  <div class="abs rule" style="left:185px;top:233px;width:987px"></div>

  <div class="abs section" style="left:187px;top:263px">BORROWER ONE</div>
  <div class="abs field focus" style="left:185px;top:303px;width:464px;--lw:136px"><span class="ic"><svg width="12" height="15"><circle cx="6" cy="4" r="3.3" fill="#1a9fe0"/><path d="M0 15c0-6 12-6 12 0z" fill="#1a9fe0"/></svg></span><span class="lbl">Borrower&nbsp;&nbsp;1:</span><span class="val">Daniel Harlow</span></div>
  <div class="abs field" style="left:710px;top:304px;width:463px;--lw:112px"><span class="ic"><svg width="12" height="16"><path d="M6 15C2 9 1 7 1 5a5 5 0 0110 0c0 2-1 4-5 10z" fill="none" stroke="#9aa3ab" stroke-width="1.4"/><circle cx="6" cy="5" r="1.8" fill="#9aa3ab"/></svg></span><span class="lbl">Address:</span><span class="val">482 Orbit Ln., Fairmont, CA 90000</span></div>
  <div class="abs rule" style="left:185px;top:374px;width:988px"></div>
  <div class="abs field" style="left:185px;top:402px;width:463px;--lw:96px"><span class="ic"><svg width="18" height="18"><circle cx="9" cy="9" r="8" fill="none" stroke="#b2bac1"/><path d="M6 5l2 2-1 1c1 2 2 3 3 3l1-1 2 2-2 1c-3 0-6-3-6-6z" fill="#b2bac1"/></svg></span><span class="lbl">Phone:</span><span class="val">111-111-1111</span></div>
  <div class="abs field" style="left:710px;top:402px;width:463px;--lw:112px"><span class="ic"><svg width="18" height="12"><rect x="1" y="1" width="16" height="10" fill="none" stroke="#9aa3ab" stroke-width="1.2"/><path d="M1 1l8 6 8-6" fill="none" stroke="#9aa3ab" stroke-width="1.2"/></svg></span><span class="lbl">Email:</span><span class="val">daniel@mailbox.com</span></div>

  <div class="abs section" style="left:190px;top:509px">BORROWER TWO</div>
  <div class="abs field" style="left:186px;top:547px;width:463px;--lw:136px"><span class="ic"><svg width="12" height="15"><circle cx="6" cy="4" r="3.3" fill="#a9b1b8"/><path d="M0 15c0-6 12-6 12 0z" fill="#a9b1b8"/></svg></span><span class="lbl">Borrower&nbsp;&nbsp;2:</span><span class="val">Grace Harlow</span></div>
  <div class="abs field" style="left:711px;top:547px;width:463px;--lw:112px"><span class="ic"><svg width="12" height="16"><path d="M6 15C2 9 1 7 1 5a5 5 0 0110 0c0 2-1 4-5 10z" fill="none" stroke="#9aa3ab" stroke-width="1.4"/><circle cx="6" cy="5" r="1.8" fill="#9aa3ab"/></svg></span><span class="lbl">Address:</span><span class="val">482 Orbit Ln., Fairmont, CA 90000</span></div>
  <div class="abs rule" style="left:185px;top:617px;width:988px"></div>
  <div class="abs field" style="left:186px;top:645px;width:463px;--lw:96px"><span class="ic"><svg width="18" height="18"><circle cx="9" cy="9" r="8" fill="none" stroke="#b2bac1"/><path d="M6 5l2 2-1 1c1 2 2 3 3 3l1-1 2 2-2 1c-3 0-6-3-6-6z" fill="#b2bac1"/></svg></span><span class="lbl">Phone:</span><span class="val">111-111-1111</span></div>
  <div class="abs field" style="left:711px;top:645px;width:463px;--lw:112px"><span class="ic"><svg width="18" height="12"><rect x="1" y="1" width="16" height="10" fill="none" stroke="#9aa3ab" stroke-width="1.2"/><path d="M1 1l8 6 8-6" fill="none" stroke="#9aa3ab" stroke-width="1.2"/></svg></span><span class="lbl">Email:</span><span class="val">daniel@mailbox.com</span></div>

  <div class="abs section" style="left:192px;top:738px">DETAILS</div>
  <div class="abs field" style="left:187px;top:777px;width:463px;--lw:151px"><span class="ic"><svg width="12" height="15"><circle cx="6" cy="4" r="3.3" fill="#a9b1b8"/><path d="M0 15c0-6 12-6 12 0z" fill="#a9b1b8"/></svg></span><span class="lbl">Aplication:</span><span class="val">Joint</span></div>
  <div class="abs field" style="left:712px;top:777px;width:463px;--lw:141px"><span class="ic"><svg width="12" height="16"><path d="M6 15C2 9 1 7 1 5a5 5 0 0110 0c0 2-1 4-5 10z" fill="none" stroke="#9aa3ab" stroke-width="1.4"/><circle cx="6" cy="5" r="1.8" fill="#9aa3ab"/></svg></span><span class="lbl">Relationship:</span><span class="val">Husband &amp; Wife</span></div>

  <div class="abs section" style="left:191px;top:887px">MORE OPTIONS</div>
  <div class="abs field" style="left:187px;top:926px;width:463px;--lw:181px"><span class="ic"><svg width="14" height="16"><rect x="1" y="1" width="12" height="14" fill="none" stroke="#a0a9b1"/><path d="M4 5h6M4 8h6M4 11h6" stroke="#a0a9b1"/></svg></span><span class="lbl">New Title Holders:</span><span class="val">Joint</span></div>
  <div class="abs pill"><span class="ic"><svg width="22" height="22"><circle cx="11" cy="11" r="10" fill="#b9c1c8"/><path d="M11 6v10M6 11h10" stroke="#fff" stroke-width="2"/></svg></span>Add Borrower</div>
  <div class="abs rule" style="left:185px;top:996px;width:990px"></div>
  <div class="abs field" style="left:188px;top:1024px;width:463px;--lw:151px"><span class="ic"><svg width="14" height="16"><rect x="1" y="1" width="12" height="14" fill="none" stroke="#a0a9b1"/><path d="M4 5h6M4 8h6M4 11h6" stroke="#a0a9b1"/></svg></span><span class="lbl">Lead Stat:</span><span class="val">3</span></div>
  <div class="abs field" style="left:713px;top:1024px;width:463px;--lw:141px"><span class="ic"><svg width="14" height="16"><rect x="1" y="1" width="12" height="14" fill="none" stroke="#a0a9b1"/><path d="M4 5h6M4 8h6M4 11h6" stroke="#a0a9b1"/></svg></span><span class="lbl">Demo Stat:</span><span class="val dark">4</span></div>

  <div class="abs alert">This is an Alert Box<p>Lorem ipsum dolor sit amet, con-<br>sectetur adipisicing <u>email us</u>.</p></div>

  <div class="abs footer"></div>
  <div class="abs status">Form Status<div class="sub">You almost finish... <b>13/17</b></div></div>
  <div class="abs bar"><i></i></div>
  <div class="abs save">Save</div>
</div>
</body>
</html>
```